Menu board for car wash

I need to have a menu board designed for my car wash. I would like for it to replicate the attached graphics of other menu boards other car washes are using. The menu board will be printed locally and be cut out with a router. I want the menu board to clearly show what they are buying and promote buying the top wash package. I also want "the Works" package to show that you can buy a monthly plan for $23.95 and receive this wash unlimited times per month. I have attached my menu that i have now (Kellingtonmenu). I would like for this new menu to have the same wording as the previous menu for the wash packages. The only addition is a new wash package "Summit Sparkle" which is now the top wash package. The new menu i would like to have going vertical and I would like my logo on the top. This menu would be 8' high and 4'wide.

Target Market(s)

Looking to have this menu be attractive and inviting. The top package should stand out the most and the lowest package should barely be noticeable ( basic wash)
I am targeting customer from the ages of 16-65 years old.

Industry/Entity Type

Automotive

Font styles to use
Serif
Sans Serif
Decorative
Other font styles liked:
• any font that flows with the design

Colors

Designer to choose colors to be used in the design.

Requirements
Must have
• This menu will be die cut out. It must fit in a 8' x 4' vertical art board.
• The wash packages will need to go from top to bottom
• They should be listed as follows
• Summit Sparkle $18
• The Works $13 ( also add Unlimited for $23.95)
• Deluxe $10
• Basic $8
• I would like to have an extras section also added just like my original menu. This can be at the bottom of the menu If you have any cool graphics that go with my theme or washes please feel free.
• The new Summit Sparkle wash will have the following included:
• Presoak
• Bug Treatment
• wheel cleaner
• Undercarriage wash
• Triple Foam Polish
• Clear Coat Protectant
• Hot Wax Treatment ( you can use graphic that is on my old menu for this item)
• Tire Shine ( You can use the Storm Glide logo)
• Hand Towel Dried
Nice to have
• Incorporate my business hours also on the menu
• the hours are:
• Monday-Saturday 8:00 Am-6:00 Pm
• Sunday 8:00 Am-5:00 Pm
• Weather may effect these hours
Should not have
• Text should be clearly visable so anyone car read it easily

```html
<!DOCTYPE html>
<html lang="en">
<head>
<meta charset="utf-8">
<title>Kellington Car Wash Menu Board</title>
<link href="https://fonts.googleapis.com/css2?family=Luckiest+Guy&family=Oswald:wght@500;700&family=Roboto+Condensed:wght@400;700&display=swap" rel="stylesheet">
<style>
  :root{
    --backdrop:#8d8d8d;
    --red:#e1252b;
    --yellow:#f8c51b;
    --white:#ffffff;
    --ink:#1b1b1b;
    --sky:#bfe6f7;
    --water-deep:#2f8fd0;
    --water-light:#cdeefe;
  }
  *{box-sizing:border-box;margin:0;padding:0}
  html,body{width:865px;height:1200px;overflow:hidden}
  body{background:var(--backdrop);font-family:"Roboto Condensed",Arial,sans-serif;position:relative}
  .abs{position:absolute}

  /* Header sign */
  .sign{left:58px;top:22px;width:690px;height:205px;background:var(--sky);border:9px solid var(--yellow);border-radius:18px;display:flex;align-items:center;justify-content:center}
  .sign-band{background:var(--yellow);border-radius:10px;padding:8px 40px;text-align:center}
  .brand-name{font-family:"Oswald",sans-serif;font-weight:700;color:var(--red);text-transform:uppercase;line-height:1;white-space:nowrap;display:flex;flex-direction:column;align-items:center}
  .brand-top{font-size:46px;letter-spacing:2px}
  .brand-main{font-size:84px;letter-spacing:1px}

  /* Package panels */
  .panel{background:var(--red);border:7px solid var(--yellow);border-radius:26px;color:var(--white)}
  .tab{background:var(--yellow);border-radius:14px;color:var(--red);font-family:"Luckiest Guy",Impact,"Arial Black",sans-serif;font-weight:400;text-transform:uppercase;line-height:1;display:flex;align-items:center;white-space:nowrap}
  .features{list-style:none;font-weight:700}
  .features li{display:flex;align-items:center;gap:8px;line-height:1.25;white-space:nowrap}
  .tick{width:22px;height:22px;flex:none}
  .price{border-radius:50%;display:flex;align-items:center;justify-content:center;font-family:"Oswald",sans-serif;font-weight:700;line-height:1;flex:none}

  .top-pkg{left:58px;top:250px;width:775px;height:318px}
  .top-pkg .tab{position:absolute;left:18px;top:16px;width:725px;height:72px;padding-left:22px;font-size:54px}
  .top-pkg .col{position:absolute;top:102px;font-size:26px}
  .top-pkg .col-a{left:40px}
  .top-pkg .col-b{left:340px}
  .hot-wax{left:34px;top:246px;width:190px;height:46px;background:var(--yellow);border-radius:8px;color:var(--red);font-family:"Oswald",sans-serif;font-weight:700;font-size:21px;display:flex;align-items:center;justify-content:center}
  .tire-shine{left:300px;top:222px;display:flex;flex-direction:column;align-items:center;gap:4px}
  .tire-brand{background:var(--ink);color:var(--white);font-family:"Oswald",sans-serif;font-weight:700;font-size:22px;padding:3px 16px;border-radius:6px}
  .tire-label{font-family:"Oswald",sans-serif;font-weight:700;font-size:22px;color:var(--white);line-height:1}
  .top-pkg .price{right:22px;top:146px;width:150px;height:150px;background:var(--white);border:9px solid var(--yellow);color:var(--ink);font-size:62px}

  .works{left:62px;top:580px;width:530px;height:192px}
  .works .tab{position:absolute;left:16px;top:14px;width:360px;height:56px;padding-left:20px;font-size:44px}
  .works .offer{position:absolute;left:28px;top:80px;font-size:23px;line-height:1.22;font-weight:700}
  .works .offer .unlimited{color:var(--yellow);font-size:24px;display:block;margin-top:2px}
  .works .price{right:18px;top:44px;width:104px;height:104px;background:var(--red);border:7px solid var(--white);color:var(--white);font-size:46px}

  .deluxe{left:62px;top:782px;width:505px;height:180px}
  .deluxe .tab{position:absolute;left:16px;top:14px;height:56px;padding:0 10px 0 18px;font-size:44px;gap:24px}
  .deluxe .tab .price{width:48px;height:48px;background:var(--yellow);border:3px solid var(--red);color:var(--ink);font-size:20px}
  .deluxe .col{position:absolute;top:80px;font-size:22px}
  .deluxe .col-a{left:26px}
  .deluxe .col-b{left:262px}

  .basic{left:62px;top:972px;width:460px;height:82px;display:flex;align-items:center;gap:22px;padding:0 14px}
  .basic .tab{height:50px;padding:0 16px;font-size:40px}
  .basic .features{font-size:18px}
  .basic .features li{line-height:1.15}
  .basic .features .tick{width:15px;height:15px}
  .basic .price{margin-left:auto;width:60px;height:60px;background:var(--red);border:4px solid var(--white);color:var(--white);font-size:28px}

  /* Hours */
  .hours{left:62px;top:1062px;width:740px;height:128px;border:6px solid var(--yellow);border-radius:18px;background:linear-gradient(180deg,var(--water-light),var(--water-deep));display:flex;align-items:center;justify-content:center}
  .hours-card{background:var(--white);border-radius:10px;width:380px;padding:6px 0 8px;text-align:center;color:var(--ink)}
  .hours-title{background:var(--red);color:var(--white);font-family:"Oswald",sans-serif;font-weight:700;font-size:24px;margin:0 8px 4px;border-radius:6px}
  .hours-row{display:flex;justify-content:space-between;padding:0 22px;font-size:17px}
  .hours-note{font-size:13px;margin-top:2px}

  .attendant{left:604px;top:590px;width:226px;height:464px;border-radius:110px 110px 30px 30px;background:linear-gradient(180deg,#f4c9a0 0%,#4fb6e4 30%,#2a7fc1 100%)}
</style>
</head>
<body>
  <header class="sign abs">
    <div class="sign-band">
      <h1 class="brand-name"><span class="brand-top">Kellington</span><span class="brand-main">Car Wash</span></h1>
    </div>
  </header>

  <section class="panel top-pkg abs">
    <h2 class="tab">Summit Sparkle</h2>
    <ul class="features col col-a">
      <li><svg class="tick" viewBox="0 0 24 24"><path d="M3 13l6 6L21 5" fill="none" stroke="#f8c51b" stroke-width="4"/></svg>Presoak</li>
      <li><svg class="tick" viewBox="0 0 24 24"><path d="M3 13l6 6L21 5" fill="none" stroke="#f8c51b" stroke-width="4"/></svg>Bug Treatment</li>
      <li><svg class="tick" viewBox="0 0 24 24"><path d="M3 13l6 6L21 5" fill="none" stroke="#f8c51b" stroke-width="4"/></svg>wheel cleaner</li>
      <li><svg class="tick" viewBox="0 0 24 24"><path d="M3 13l6 6L21 5" fill="none" stroke="#f8c51b" stroke-width="4"/></svg>Undercarriage wash</li>
    </ul>
    <ul class="features col col-b">
      <li><svg class="tick" viewBox="0 0 24 24"><path d="M3 13l6 6L21 5" fill="none" stroke="#f8c51b" stroke-width="4"/></svg>Triple Foam Polish</li>
      <li><svg class="tick" viewBox="0 0 24 24"><path d="M3 13l6 6L21 5" fill="none" stroke="#f8c51b" stroke-width="4"/></svg>Clear Coat Protectant</li>
      <li><svg class="tick" viewBox="0 0 24 24"><path d="M3 13l6 6L21 5" fill="none" stroke="#f8c51b" stroke-width="4"/></svg>Hand Towel Dried</li>
    </ul>
    <div class="hot-wax abs">Hot Wax Treatment</div>
    <div class="tire-shine abs">
      <span class="tire-brand">Storm Glide</span>
      <span class="tire-label">TIRE SHINE</span>
    </div>
    <div class="price abs">$18</div>
  </section>

  <section class="panel works abs">
    <h2 class="tab">The Works</h2>
    <p class="offer">Buy A Monthly Plan For $23.95<br>and receive this wash<span class="unlimited">UNLIMITED TIMES PER MONTH</span></p>
    <div class="price abs">$13</div>
  </section>

  <section class="panel deluxe abs">
    <h2 class="tab">Deluxe <span class="price">$10</span></h2>
    <ul class="features col col-a">
      <li><svg class="tick" viewBox="0 0 24 24"><path d="M3 13l6 6L21 5" fill="none" stroke="#f8c51b" stroke-width="4"/></svg>Presoak</li>
      <li><svg class="tick" viewBox="0 0 24 24"><path d="M3 13l6 6L21 5" fill="none" stroke="#f8c51b" stroke-width="4"/></svg>wheel cleaner</li>
      <li><svg class="tick" viewBox="0 0 24 24"><path d="M3 13l6 6L21 5" fill="none" stroke="#f8c51b" stroke-width="4"/></svg>Undercarriage wash</li>
    </ul>
    <ul class="features col col-b">
      <li><svg class="tick" viewBox="0 0 24 24"><path d="M3 13l6 6L21 5" fill="none" stroke="#f8c51b" stroke-width="4"/></svg>Triple Foam Polish</li>
      <li><svg class="tick" viewBox="0 0 24 24"><path d="M3 13l6 6L21 5" fill="none" stroke="#f8c51b" stroke-width="4"/></svg>Clear Coat</li>
      <li><svg class="tick" viewBox="0 0 24 24"><path d="M3 13l6 6L21 5" fill="none" stroke="#f8c51b" stroke-width="4"/></svg>Hand Towel Dry</li>
    </ul>
  </section>

  <section class="panel basic abs">
    <h2 class="tab">Basic</h2>
    <ul class="features">
      <li><svg class="tick" viewBox="0 0 24 24"><path d="M3 13l6 6L21 5" fill="none" stroke="#f8c51b" stroke-width="4"/></svg>Presoak</li>
      <li><svg class="tick" viewBox="0 0 24 24"><path d="M3 13l6 6L21 5" fill="none" stroke="#f8c51b" stroke-width="4"/></svg>Wash</li>
      <li><svg class="tick" viewBox="0 0 24 24"><path d="M3 13l6 6L21 5" fill="none" stroke="#f8c51b" stroke-width="4"/></svg>Dry</li>
    </ul>
    <div class="price">$8</div>
  </section>

  <section class="hours abs" role="img" aria-label="Splashing water background behind the business hours">
    <div class="hours-card">
      <h3 class="hours-title">BUSINESS HOURS</h3>
      <div class="hours-row"><span>Monday-Saturday</span><span>8:00 Am-6:00 Pm</span></div>
      <div class="hours-row"><span>Sunday</span><span>8:00 Am-5:00 Pm</span></div>
      <p class="hours-note">(Weather may effect these hours)</p>
    </div>
  </section>

  <div class="attendant abs" role="img" aria-label="Illustration of a car wash attendant in blue overalls holding a pressure washer wand"></div>
</body>
</html>
```